New Webpage for High Class Expert Witness Services Company

We are looking for a minimalist design for a webpage that just has our logo and an entry form offer to connect with one of our Liaisons.
The entry form should just ask for Name, Email, Contact Info and Description of Project.

Company Name is: The Marlow Crest Advisory Services

Number of Pages Required

1 page

```html
<!DOCTYPE html>
<html lang="en">
<head>
<meta charset="utf-8">
<title>Marlow Crest Advisory Services – Connect with a Liaison</title>
<link href="https://fonts.googleapis.com/css2?family=Cinzel:wght@400;500&family=Figtree:wght@400;500;600&display=swap" rel="stylesheet">
<style>
  :root{
    --bg-edge:#121212;
    --bg-glow:#2c2c2c;
    --field-bg:#2a2a2a;
    --field-border:#363636;
    --text-light:#ececec;
    --text-label:#e2e2e2;
    --text-placeholder:#6f6f6f;
    --text-muted:#6a6a6a;
    --btn-top:#ffffff;
    --btn-bottom:#a9a9ae;
    --btn-text:#111111;
  }
  *{box-sizing:border-box;margin:0;padding:0}
  html,body{width:1200px;height:810px;overflow:hidden}
  body{
    position:relative;
    background:radial-gradient(ellipse 520px 420px at 600px 400px,var(--bg-glow) 0%,#1d1d1d 60%,var(--bg-edge) 100%);
    font-family:"Figtree",sans-serif;
    color:var(--text-light);
  }
  .brand{
    position:absolute;left:171px;top:52px;
    display:flex;align-items:center;gap:12px;
  }
  .brand-mark{width:34px;height:34px;background:var(--text-light)}
  .brand-name{
    font-family:"Cinzel",serif;font-weight:500;font-size:24px;
    line-height:1.1;color:var(--text-light);letter-spacing:1px;
  }
  .btn{
    display:flex;align-items:center;justify-content:center;
    background:linear-gradient(180deg,var(--btn-top) 0%,#e4e4e6 45%,var(--btn-bottom) 100%);
    color:var(--btn-text);font-family:"Figtree",sans-serif;font-weight:600;
    border:none;
  }
  .btn-contact{position:absolute;left:913px;top:56px;width:112px;height:40px;font-size:13px}
  .intro{position:absolute;left:0;top:188px;width:1200px;text-align:center}
  .intro-title{font-family:"Cinzel",serif;font-weight:400;font-size:26px;letter-spacing:.5px;color:#f2f2f2}
  .intro-sub{margin-top:6px;font-size:13px;font-weight:500;color:var(--text-light)}
  .contact-form{position:absolute;left:317px;top:275px;width:562px}
  .field{
    height:55px;margin-bottom:8px;padding:13px 13px 0;
    background:var(--field-bg);border:1px solid var(--field-border);
  }
  .field-message{height:78px}
  .field-label{display:block;font-size:12px;font-weight:500;color:var(--text-label)}
  .field-placeholder{display:block;margin-top:2px;font-size:11.5px;color:var(--text-placeholder)}
  .consent{display:flex;gap:8px;margin-top:16px}
  .consent-box{flex:none;width:18px;height:18px;margin-top:3px;border:1px solid #e0e0e0}
  .consent-text{font-size:11.5px;line-height:18px;color:var(--text-muted)}
  .consent-text u{font-weight:600;color:#888}
  .btn-submit{width:180px;height:47px;margin:20px auto 0;font-size:14px}
</style>
</head>
<body>
  <header>
    <div class="brand">
      <div class="brand-mark"></div>
      <div class="brand-name">Marlow Crest<br>Advisory Services</div>
    </div>
    <div class="btn btn-contact">Contact Us</div>
  </header>

  <section class="intro">
    <h1 class="intro-title">CONNECT WITH ONE OF OUR LIAISONS</h1>
    <p class="intro-sub">Tell us about your project and a member of our team will be in touch with you.</p>
  </section>

  <form class="contact-form">
    <div class="field"><span class="field-label">Name</span><span class="field-placeholder">Enter Your Full Name</span></div>
    <div class="field"><span class="field-label">Email</span><span class="field-placeholder">your@example.com</span></div>
    <div class="field"><span class="field-label">Contact No.</span><span class="field-placeholder">Enter Your Phone Number</span></div>
    <div class="field field-message"><span class="field-label">How Can We Help?</span><span class="field-placeholder">Description of Project.</span></div>
    <div class="consent">
      <div class="consent-box"></div>
      <p class="consent-text">By checking this box, I give my consent to The Marlow Crest Advisory Services to manage the information on the form above for the purpose of communication. View our <u>Privacy Policy.</u></p>
    </div>
    <div class="btn btn-submit">Submit and Continue</div>
  </form>
</body>
</html>
```